Website Design For our Tour Company

We need a face lift on our current website. I want it to look the best! Lots of videos. An easy to use website to obtain easy conversions. I want people to feel like they are on the tour just by looking at our website. My current website is just bland and unprofessional looking. I want it to be incredibly mobile friendly and look great on the desk top. Our current website is https://www.halvorsenelitejaunts.example/
I would like there to be an option where the viewer can select what language they would like to read in. Im hoping you can pull a-lot of media and videos from out lumenfeed page. Im not happy with most of my descriptions for the product and tours we offer. Looking for professional help.

Our two main activities are Summer and Winter Tours
In The Summer the main things we do our Jet Boat & Jet Ski Tours.

In The Winter our main tour is luxury first class Aurora Viewing. I Would like to see a-lot of aurora video/photos as I believe that gets peoples attention!

Target Market(s)

Travelers from china and around the world

Coding

Coded - Design and coding required

Number of Pages Required

5+ page

Requirements
Must have
• be able to select what when language you would like to read the website in.
Nice to have
• The overall look and feel I want for the website is luxury, fancy, royalty. Think Harold Pemberly. I like the Luxury gold colors. I need the website to look ridiculously professional

incorporate Lots of Aurora photos / videos as one of our main tours is Aurora

```html
<!DOCTYPE html>
<html lang="en">
<head>
<meta charset="utf-8">
<title>Halvorsen Elite Jaunts</title>
<link href="https://fonts.googleapis.com/css2?family=Merriweather:ital,wght@0,300;0,400;1,300&family=Montserrat:wght@400;500;600;700&display=swap" rel="stylesheet">
<style>
:root{
  --bg:#1b1b1b;
  --panel:#121212;
  --gold:#b89a5c;
  --gold-soft:#8f7748;
  --text:#e8e4dc;
  --muted:#b5b0a6;
  --line:#4a4033;
}
*{margin:0;padding:0;box-sizing:border-box}
html,body{width:1200px;height:4280px;overflow:hidden;background:var(--bg)}
body{position:relative;font-family:'Montserrat',sans-serif;color:var(--text)}
.abs{position:absolute}
.photo{position:absolute;overflow:hidden}

.topbar{left:0;top:0;width:1200px;height:36px;border-bottom:1px solid var(--line);background:#0f0f0f;z-index:3}
.topbar .tag{position:absolute;left:76px;top:12px;font-family:'Merriweather',serif;font-size:10px;letter-spacing:3px;color:var(--gold-soft);text-transform:uppercase}
.topbar .lang{position:absolute;right:72px;top:11px;font-size:10px;letter-spacing:1px;color:var(--muted)}
.navbar{left:0;top:36px;width:1200px;height:76px;z-index:3}
.brand{position:absolute;display:flex;align-items:center;gap:10px}
.brand .mark{width:40px;height:40px;border:1.5px solid var(--gold);border-radius:50%}
.brand .name{font-family:'Merriweather',serif;font-size:18px;font-weight:400;color:var(--text);line-height:1.1;letter-spacing:1px}
.brand .name small{display:block;font-size:8px;letter-spacing:4px;color:var(--text)}
.menu{position:absolute;display:flex;gap:36px;font-size:11px;font-weight:600;letter-spacing:1.5px;text-transform:uppercase;color:#8d8880}
.menu .on{color:#fff}
.phone{position:absolute;display:flex;align-items:center;gap:10px;font-size:12px;font-weight:700;color:#fff}
.ring{width:26px;height:26px;border:1px solid var(--gold-soft);border-radius:50%;display:flex;align-items:center;justify-content:center}

.hero{left:0;top:0;width:1200px;height:612px;background:linear-gradient(180deg,#1c2418 0%,#3e4a2c 40%,#56673a 62%,#6f7a74 78%,#8a9096 100%)}
.hero::after{content:"";position:absolute;inset:0;background:linear-gradient(180deg,rgba(0,0,0,.55),rgba(0,0,0,.15) 40%,rgba(0,0,0,.1))}
.card{position:absolute;background:rgba(10,10,10,.9);padding:40px 36px}
.eyebrow{font-size:12px;letter-spacing:6px;color:var(--gold);text-transform:uppercase;font-weight:600}
.hero-title{font-family:'Merriweather',serif;font-weight:300;font-size:27px;letter-spacing:3px;line-height:1.1;color:#fff;margin-top:6px}
.body-s{font-size:10.5px;line-height:1.45;color:var(--muted)}
.btn{display:inline-flex;align-items:center;gap:10px;background:#0b0b0b;border:1px solid #222;color:var(--gold);font-size:11px;font-weight:600;letter-spacing:3px;text-transform:uppercase;padding:12px 24px}
.dots{left:1121px;top:285px;display:flex;flex-direction:column;gap:14px}
.dots i{width:8px;height:8px;border-radius:50%;background:#9a9a9a;display:block}
.dots i.on{width:14px;height:14px;margin-left:-3px;border:2px solid var(--gold);background:transparent}

.h2{font-family:'Merriweather',serif;font-weight:300;font-size:25px;color:#fff;text-align:center;width:1200px;left:0}
.label{font-size:19px;letter-spacing:10px;font-weight:600;text-transform:uppercase;color:var(--gold);display:flex;align-items:center;gap:14px}
.label::before{content:"";width:26px;height:1px;background:var(--gold)}
.lead{font-family:'Merriweather',serif;font-size:14px;line-height:1.55;color:#eee;font-weight:300}
.play{position:absolute;width:60px;height:60px;border-radius:50%;background:#111;display:flex;align-items:center;justify-content:center;box-shadow:0 0 0 4px rgba(0,0,0,.3)}
.arrow{position:absolute;width:40px;height:40px;border-radius:50%;background:rgba(20,20,20,.7);display:flex;align-items:center;justify-content:center}
.overcap{position:absolute;font-size:10.5px;line-height:1.45;color:#e2e2e2}
.field{position:absolute;left:123px;width:311px;height:53px;border:1px solid #6a6a6a;font-size:11px;color:#ddd;padding:19px 20px}
.bullets li{list-style:none;position:relative;padding-left:18px;font-size:11px;line-height:1.45;color:var(--muted);margin-bottom:16px}
.bullets li::before{content:"";position:absolute;left:0;top:5px;width:6px;height:6px;border-radius:50%;background:var(--muted)}
</style>
</head>
<body>

<div class="abs topbar"><span class="tag">Taking you where the trail leads</span><span class="lang">EN ▾</span></div>
<header class="abs navbar">
  <div class="brand" style="left:76px;top:12px"><span class="mark"></span><span class="name">HALVORSEN<small>ELITE JAUNTS</small></span></div>
  <nav class="menu" style="left:340px;top:31px"><span class="on">Home</span><span>Summer Tours</span><span>Winter Tours</span><span>Book Online</span><span>More</span></nav>
  <div class="phone" style="left:928px;top:24px"><span class="ring"><svg width="12" height="12" viewBox="0 0 24 24"><path d="M6.6 10.8a15 15 0 006.6 6.6l2.2-2.2a1 1 0 011-.25 11 11 0 003.5.56 1 1 0 011 1V20a1 1 0 01-1 1A17 17 0 013 4a1 1 0 011-1h3.5a1 1 0 011 1 11 11 0 00.56 3.5 1 1 0 01-.25 1z" fill="#b89a5c"/></svg></span>555-014-2780</div>
  <div class="ring" style="position:absolute;left:1106px;top:24px" aria-label="lumenfeed"></div>
</header>

<section class="photo hero" role="img" aria-label="Three guests raising paddles in kayaks on a lake in front of a large sign and forest"></section>
<div class="card" style="left:73px;top:241px;width:357px;height:241px;z-index:2">
  <div class="eyebrow">Incredible</div>
  <div class="hero-title">Aurora Viewing<br>Adventure</div>
  <p class="body-s" style="margin-top:20px;width:290px">You'll jump right into the action of our weekly basketball coaching clinics, where we do drills and plays for two hours with 60 kids. There are only three of us for all of the kid</p>
  <div class="btn" style="margin-top:14px">Begin Adventure <svg width="16" height="10"><path d="M0 5h14M10 1l4 4-4 4" stroke="#b89a5c" fill="none"/></svg></div>
</div>
<div class="abs dots" style="z-index:2"><i></i><i class="on"></i><i></i></div>

<h2 class="abs h2" style="top:670px">Great Deals On Guided Tours</h2>
<div class="abs label" style="left:76px;top:764px">Summer Tours</div>

<div class="photo" style="left:73px;top:819px;width:497px;height:290px;background:linear-gradient(180deg,#3f5e2a,#557c33 45%,#3a3f20 70%,#1b1a12)" role="img" aria-label="Guest paddling a kayak on a forest lake"></div>
<div class="overcap" style="left:100px;top:1050px;width:440px">Lorem ipsum dolor sit amet, consectetur adipiscing elit. Aenean sed efficitur nunc. Nulla sed leo nulla. In lobortis, ipsum lacinia vulputate feugiat.</div>
<div class="play" style="left:535px;top:936px"><svg width="14" height="16"><path d="M0 0l14 8-14 8z" fill="#ddd"/></svg></div>
<div class="abs" style="left:648px;top:848px;width:400px">
  <p class="lead">Orci varius natoque penatibus et magnis dis parturient montes, nascetur ridiculus mus. Cras tincidunt sed elit at posuere. Sed vestibulum consectetur odio id ultricies.</p>
  <p class="body-s" style="margin-top:18px">Lorem ipsum dolor sit amet, consectetur adipiscing elit. Aenean sed efficitur nunc. Nulla sed leo nulla. In lobortis, ipsum lacinia vulputate feugiat. Nullam venenatis, enim sit amet malesuada commodo, diam tortor efficitur purus, sit amet commodo purus tortor sit amet augue. Vestibulum quis efficitur quam, a volutpat dolor.</p>
  <div class="btn" style="margin-top:22px">Begin Adventure <svg width="16" height="10"><path d="M0 5h14M10 1l4 4-4 4" stroke="#b89a5c" fill="none"/></svg></div>
</div>

<div class="photo" style="left:73px;top:1132px;width:341px;height:214px;background:linear-gradient(180deg,#8a8680,#5b5a58 50%,#2a2828)" role="img" aria-label="View over jet ski handlebars toward a riverboat"></div>
<div class="photo" style="left:432px;top:1132px;width:341px;height:214px;background:linear-gradient(180deg,#7d95a6,#5d7a4c 45%,#5c6a78 75%,#2a3a52)" role="img" aria-label="Two guests riding a jet ski on a lake"></div>
<div class="photo" style="left:789px;top:1132px;width:341px;height:214px;background:linear-gradient(180deg,#4c6a2e,#6d7a44 40%,#9a6b2c 75%,#4b4a3a)" role="img" aria-label="Guest in a yellow kayak on calm water"></div>
<div class="arrow" style="left:58px;top:1222px"><svg width="14" height="10"><path d="M14 5H1M5 1L1 5l4 4" stroke="#aaa" fill="none"/></svg></div>
<div class="arrow" style="left:1113px;top:1222px"><svg width="14" height="10"><path d="M0 5h13M9 1l4 4-4 4" stroke="#aaa" fill="none"/></svg></div>

<div class="photo" style="left:0;top:1368px;width:1200px;height:385px;background:linear-gradient(180deg,#5a3a48,#3f2a36 45%,#2a2a30 70%,#1e1e22)" role="img" aria-label="Rider on a jet ski spraying water in front of a forest and large sign"></div>
<div class="arrow" style="left:57px;top:1541px"><svg width="14" height="10"><path d="M14 5H1M5 1L1 5l4 4" stroke="#aaa" fill="none"/></svg></div>
<div class="arrow" style="left:1113px;top:1541px"><svg width="14" height="10"><path d="M0 5h13M9 1l4 4-4 4" stroke="#aaa" fill="none"/></svg></div>
<p class="abs lead" style="left:280px;top:1644px;width:640px;text-align:center;font-size:14.5px">Orci varius natoque penatibus et magnis dis parturient montes, nascetur ridiculus mus. Cras tincidunt sed elit at posuere. Sed vestibulum consectetur odio id ultricies.</p>
<div class="abs" style="left:0;top:1753px;width:1200px;height:1px;background:var(--line)"></div>
<div class="play" style="left:570px;top:1707px"><svg width="14" height="16"><path d="M0 0l14 8-14 8z" fill="#ddd"/></svg></div>

<div class="abs label" style="left:96px;top:1829px">Winter Tours</div>
<div class="abs" style="left:145px;top:1911px;width:395px">
  <p class="lead">Orci varius natoque penatibus et magnis dis parturient montes, nascetur ridiculus mus. Cras tincidunt sed elit at posuere. Sed vestibulum consectetur odio id ultricies.</p>
  <p class="body-s" style="margin-top:18px">Lorem ipsum dolor sit amet, consectetur adipiscing elit. Aenean sed efficitur nunc. Nulla sed leo nulla. In lobortis, ipsum lacinia vulputate feugiat. Nullam venenatis, enim sit amet malesuada commodo, diam tortor efficitur purus, sit amet commodo purus tortor sit amet augue. Vestibulum quis efficitur quam, a volutpat dolor.</p>
  <div class="btn" style="margin-top:22px">Begin Adventure <svg width="16" height="10"><path d="M0 5h14M10 1l4 4-4 4" stroke="#b89a5c" fill="none"/></svg></div>
</div>
<div class="photo" style="left:633px;top:1885px;width:497px;height:287px;background:linear-gradient(180deg,#7a7c92,#8a6a60 40%,#4a3030 75%,#1a1414)" role="img" aria-label="Two guests in warm winter clothing outdoors"></div>
<div class="play" style="left:608px;top:1999px"><svg width="14" height="16"><path d="M0 0l14 8-14 8z" fill="#ddd"/></svg></div>
<div class="overcap" style="left:660px;top:2115px;width:440px">Lorem ipsum dolor sit amet, consectetur adipiscing elit. Aenean sed efficitur nunc. Nulla sed leo nulla. In lobortis, ipsum lacinia vulputate feugiat.</div>

<div class="photo" style="left:73px;top:2196px;width:341px;height:217px;background:linear-gradient(180deg,#c8b06a,#e6c27a 35%,#b9bcc2 65%,#e8eaee)" role="img" aria-label="Mug on a snowy riverbank at golden sunset between birch trees"></div>
<div class="photo" style="left:432px;top:2196px;width:341px;height:217px;background:linear-gradient(180deg,#3e5a6e,#6e6f7e 45%,#c9cbd4 80%,#e2e4ea)" role="img" aria-label="Guests on snowshoes in a snowy forest"></div>
<div class="photo" style="left:789px;top:2196px;width:341px;height:217px;background:linear-gradient(180deg,#a6c2dc,#dfe6ee 40%,#3aa6c8 70%,#6a8aa0)" role="img" aria-label="Steaming outdoor hot tub surrounded by snow"></div>
<div class="arrow" style="left:58px;top:2285px"><svg width="14" height="10"><path d="M14 5H1M5 1L1 5l4 4" stroke="#aaa" fill="none"/></svg></div>
<div class="arrow" style="left:1113px;top:2285px"><svg width="14" height="10"><path d="M0 5h13M9 1l4 4-4 4" stroke="#aaa" fill="none"/></svg></div>

<h2 class="abs h2" style="top:2488px">Take Your Next Trip With Halvorsen Resorts, Llc</h2>
<p class="abs body-s" style="left:265px;top:2543px;width:670px;text-align:center">Halvorsen Resorts, LLC specializes in providing the best travel services in Birchmoor, Northvale. We've been in Birchmoor since 2003, creating customized itineraries for our clients based around their personal plans and preferences. In our line of work we don't only make plans, we help you build experiences and memories. Let us arrange the details of your next trip — call today for a free consultation.</p>
<div class="photo" style="left:396px;top:2651px;width:734px;height:326px;background:linear-gradient(180deg,#5a5a5e,#7a7670 35%,#2e8aa8 65%,#3a4e58)" role="img" aria-label="Lodge patio with a blue sectional sofa"></div>
<div class="play" style="left:733px;top:2785px"><svg width="14" height="16"><path d="M0 0l14 8-14 8z" fill="#ddd"/></svg></div>
<div class="card" style="left:73px;top:2692px;width:357px;height:241px;padding:48px 38px">
  <p class="lead" style="font-style:italic;color:var(--gold);font-size:13.5px">Orci varius natoque penatibus et magnis dis parturient montes, nascetur ridiculus mus. Cras tincidunt sed elit at posuere.</p>
  <div class="btn" style="margin-top:22px">Learn More <svg width="16" height="10"><path d="M0 5h14M10 1l4 4-4 4" stroke="#b89a5c" fill="none"/></svg></div>
  <div style="display:flex;gap:24px;margin-top:18px"><svg width="18" height="12"><path d="M18 6H1M6 1L1 6l5 5" stroke="#aaa" fill="none"/></svg><svg width="18" height="12"><path d="M0 6h17M12 1l5 5-5 5" stroke="#aaa" fill="none"/></svg></div>
</div>

<div class="photo" style="left:73px;top:3086px;width:291px;height:343px;background:linear-gradient(180deg,#3e5a2a,#7a8a8c 40%,#6a4a3a 70%,#2a3a1a)" role="img" aria-label="Two kayaks resting on a grassy lakeshore"></div>
<div class="photo" style="left:381px;top:3086px;width:289px;height:343px;background:radial-gradient(ellipse at 60% 35%,#3fe06a,#1a7a3a 30%,#0e1a26 70%)" role="img" aria-label="Green aurora swirling across the night sky"></div>
<div class="abs label" style="left:838px;top:3085px">About Us</div>
<div class="abs" style="left:724px;top:3162px;width:406px">
  <p class="lead" style="font-size:14px">Great Journeys. Fascinating Places.<br>Local Experts Leif, Ingrid, and Soren</p>
  <ul class="bullets" style="margin-top:18px">
    <li>Soren - Life-long Northerner - Local expert, loves the outdoors, construction, &amp; adventures</li>
    <li>Leif - Life-long Northerner - Local expert entrepreneur, loves the North, always ready for an adventure and a fun time!</li>
    <li>Ingrid - Life-long Northerner - Local expert, company cook, organizes the activities &amp; schedule. Without her we have no organization.</li>
  </ul>
  <div class="btn" style="margin-top:8px">Begin Adventure <svg width="16" height="10"><path d="M0 5h14M10 1l4 4-4 4" stroke="#b89a5c" fill="none"/></svg></div>
</div>

<div class="photo" style="left:0;top:3494px;width:1200px;height:528px;background:linear-gradient(180deg,#3a3440,#d9a64a 22%,#e6c27a 32%,#8a8aa0 55%,#c8cce0 80%,#e8ecf4)" role="img" aria-label="Snowy riverbank with birch trees at golden sunset"></div>
<div class="abs" style="left:73px;top:3628px;width:414px;height:394px;background:var(--panel)"></div>
<div class="abs label" style="left:126px;top:3674px">Contact Us</div>
<div class="field" style="top:3753px">Name</div>
<div class="field" style="top:3819px">Email</div>
<div class="field" style="top:3885px">Subject</div>
<div class="field" style="top:3951px">Message</div>
<div class="abs btn" style="left:123px;top:4022px;width:186px;justify-content:center;background:#0f0f0f">Submit <svg width="16" height="10"><path d="M0 5h14M10 1l4 4-4 4" stroke="#b89a5c" fill="none"/></svg></div>

<footer>
  <div class="brand" style="left:76px;top:4124px"><span class="mark"></span><span class="name">HALVORSEN<small>ELITE JAUNTS</small></span></div>
  <nav class="menu" style="left:340px;top:4142px"><span class="on">Home</span><span>Summer Tours</span><span>Winter Tours</span><span>Book Online</span><span>More</span></nav>
  <div class="phone" style="left:928px;top:4135px"><span class="ring"><svg width="12" height="12" viewBox="0 0 24 24"><path d="M6.6 10.8a15 15 0 006.6 6.6l2.2-2.2a1 1 0 011-.25 11 11 0 003.5.56 1 1 0 011 1V20a1 1 0 01-1 1A17 17 0 013 4a1 1 0 011-1h3.5a1 1 0 011 1 11 11 0 00.56 3.5 1 1 0 01-.25 1z" fill="#b89a5c"/></svg></span>555-014-2780</div>
  <div class="ring" style="position:absolute;left:1106px;top:4135px" aria-label="lumenfeed"></div>
  <div class="abs" style="left:0;top:4215px;width:1200px;height:1px;background:var(--line)"></div>
  <p class="abs" style="left:0;top:4241px;width:1200px;text-align:center;font-size:10px;color:var(--muted)">©2020 by Halvorsen Resorts, LLC.</p>
</footer>

</body>
</html>
```